High-End Medical Center Website Design Project

This design is part of a well thought-out project by an experienced project manager / developer. The approved wireframe is attached. Creative interpretations / suggestions based on the layout encouraged.

The design is for a new state-of-the-art medical center located in Dallas, Texas. The target audience would likely be individuals (approx. 60% female /40% male) who are the healthcare decision-makers for their families. They would likely have insurance and be inclined to seek out top-quality care.

Potential clients would choose this client over others in their industry because the medical center is physician owned, meaning it is patient-focused rather than profit-focused. The facility is brand new, featuring the latest technology. (This includes an amazing waiting room featuring WiFi and docking stations.) The physicians are hand-picked by referral only.

The look of the site should be extremely clean. We are going for a well-organized, professional look with a bit of a warm glow (interpret that however you like). Use crisp corners and the colors in the logo.

Think modern, clean with some great use of color / font.

We can get lovely photography of the medical center once construction is complete. Feel free to use an "example image" behind the Featured Area ("Physician Owned. Patient-Focused") if you like. We are open to ideas.

ONE CHANGE REQUESTED IN THE WIREFRAME:

Remove the "Connect" 1/4 page footer area and replace with a quick contact form. You may swap the "Locations" area with the form if desired. Put social media icons at the top left of the page in the top header area.

(Note: Please use social media icons that match the design rather than standard icons. We preferred not placing the icons at the top, but the client requested this. Let's not bring more attention to them than necessary.)
Updates

We're custom programming this site, so there's no need to base it on a template. Also, we would prefer not to use typical "seen everywhere" stock images.Thanks.

Industry/Entity Type

Construction

Requirements
Must have
• Follow the wireframe. This has been approved.
Nice to have
• Examples of what hover states, links or dropdowns might look like.

```html
<!DOCTYPE html>
<html lang="en">
<head>
<meta charset="utf-8">
<title>Nova Medical Center</title>
<link href="https://fonts.googleapis.com/css2?family=Roboto:wght@300;400;500&family=Roboto+Condensed:wght@300;400;700&display=swap" rel="stylesheet">
<style>
:root{
  --teal:#49a7bc;
  --teal-dark:#2f7f96;
  --teal-deep:#2b6a80;
  --orange:#f2652b;
  --grey-bg:#ececec;
  --panel:#efefef;
  --line:#e1e1e1;
  --text:#555;
  --muted:#8a8a8a;
  --navy:#1b5c9c;
  --white:#fff;
}
*{box-sizing:border-box;margin:0;padding:0}
html,body{width:847px;height:1200px;overflow:hidden;background:#fff}
body{font-family:"Roboto",sans-serif;color:var(--text)}
.page{position:relative;width:1050px;height:1487px;transform:scale(.80667);transform-origin:0 0}
.abs{position:absolute}
.topbar{left:0;top:0;width:1050px;height:27px;background:#f6f6f6;border-bottom:1px solid #eee}
.connect{left:76px;top:8px;font-size:11px;color:#aaa;display:flex;align-items:center;gap:8px}
.social{width:10px;height:10px;border-radius:50%;background:#c4c4c4}
.social.first{background:var(--orange)}
.utility{right:86px;top:6px;display:flex;gap:16px}
.brand{left:77px;top:40px;height:44px;display:flex;align-items:center;gap:10px;font-family:"Roboto Condensed",sans-serif;font-weight:700;font-size:27px;color:var(--navy);letter-spacing:.5px;white-space:nowrap}
.brand-mark{width:26px;height:26px;background:var(--teal)}
.nav{right:76px;top:60px;display:flex;gap:24px;font-family:"Roboto Condensed",sans-serif;font-size:14px;color:#666;letter-spacing:.3px}
.nav a{color:inherit;text-decoration:none}
.nav a.active{color:var(--teal)}
.hero{left:77px;top:96px;width:618px;height:409px;background:linear-gradient(90deg,#b9d3e6 0%,#e8eef3 45%,#f3f0ec 70%,#dfe5ea 100%)}
.hero-caption{left:77px;top:455px;width:618px;height:50px;background:rgba(255,255,255,.55);padding:16px 28px;font-family:"Roboto Condensed",sans-serif;font-style:italic;font-size:18px;color:var(--navy)}
.qc-head{left:695px;top:96px;width:278px;height:98px;background:var(--teal);color:#fff;text-align:center;font-family:"Roboto Condensed",sans-serif;font-weight:300}
.qc-head h2{font-weight:300;font-size:27px;margin-top:12px;letter-spacing:.5px}
.qc-phone{display:flex;justify-content:center;align-items:center;gap:10px;font-size:26px;margin-top:2px}
.qc-phone span.ic{width:30px;height:30px;border-radius:50%;border:2px solid rgba(255,255,255,.7);display:flex;align-items:center;justify-content:center}
.qc-form{left:695px;top:194px;width:278px;height:311px;background:#ebebeb}
.or{left:821px;top:179px;width:29px;height:29px;border-radius:50%;background:var(--orange);color:#fff;font-family:"Roboto Condensed",sans-serif;font-size:14px;display:flex;align-items:center;justify-content:center;border:2px solid #fff}
.field{left:723px;width:222px;height:29px;background:#fff;border:1px solid #e2e2e2;font-size:12px;color:#aaa;padding:7px 8px;font-weight:300}
.field.msg{height:93px}
.btn{background:var(--orange);color:#fff;font-family:"Roboto Condensed",sans-serif;font-weight:700;font-size:15px;display:flex;align-items:center;justify-content:center}
.submit{left:723px;top:448px;width:132px;height:33px}
.apart{left:84px;top:580px;font-family:"Roboto Condensed",sans-serif;font-size:17px;color:#666;font-style:italic}
.feature{top:531px;width:215px;height:213px;background:var(--panel);border:1px solid var(--line);text-align:center}
.feature .icon{width:60px;height:60px;border-radius:50%;background:var(--teal);margin:22px auto 0;display:flex;align-items:center;justify-content:center}
.feature h3{font-family:"Roboto Condensed",sans-serif;font-weight:400;font-size:23px;color:var(--teal);margin-top:14px}
.feature p{font-size:12.5px;font-weight:300;color:var(--muted);line-height:18px;margin:10px 14px 0}
.band{left:0;top:770px;width:1050px;height:319px;background:var(--grey-bg)}
.team{left:98px;top:812px;width:220px;height:221px;background:linear-gradient(160deg,#eef2f5,#c9dde9 50%,#f4f5f6)}
.about{left:355px;top:820px;width:310px}
h2.sec{font-family:"Roboto Condensed",sans-serif;font-weight:700;font-size:25px;color:var(--teal)}
.about p,.testi p{font-size:12px;line-height:16px;color:#555;margin-top:14px}
.about h2{margin-bottom:-4px}
.testi{left:701px;top:805px;width:267px;height:220px;background:#fff;padding:16px 30px}
.testi p{color:#777;margin-top:12px}
.testi-tail{left:905px;top:1024px}
.testi-author{left:764px;top:1038px;font-family:"Roboto Condensed",sans-serif;font-size:13px;color:#555}
.cta{left:0;top:1089px;width:1050px;height:65px;background:#fff}
.call{left:107px;top:1106px;display:flex;align-items:center;gap:8px;font-family:"Roboto Condensed",sans-serif;font-size:25px;color:var(--teal)}
.divider{left:397px;top:1113px;width:1px;height:16px;background:#ccc}
.nl-label{left:415px;top:1113px;font-family:"Roboto Condensed",sans-serif;font-size:14px;color:#555}
.nl-input{left:560px;top:1103px;width:256px;height:37px;border:1px solid #ddd;padding:11px 13px;font-size:13px;color:#999;font-weight:300}
.subscribe{left:822px;top:1103px;width:146px;height:37px;gap:10px;font-size:17px}
.footer{left:0;top:1154px;width:1050px;height:297px;background:var(--teal)}
.fcol{top:1195px;color:#fff}
.fcol h3{font-family:"Roboto Condensed",sans-serif;font-weight:400;font-size:27px;margin-bottom:12px}
.item{display:flex;gap:10px;margin-bottom:12px;font-size:12.5px;line-height:16.5px;width:170px}
.date{width:40px;height:47px;flex:none;background:var(--teal-deep);text-align:center;font-family:"Roboto Condensed",sans-serif;line-height:1}
.date b{display:block;font-size:24px;font-weight:400;padding-top:5px}
.date small{font-size:13px}
.date.plain{background:none;color:#2f7f96}
.loc{width:162px;font-size:12.5px;line-height:16px;padding-bottom:8px;margin-bottom:8px;border-bottom:1px dotted rgba(255,255,255,.55)}
.loc:last-child{border:none}
.wait{left:701px;top:1179px;width:267px;height:242px;background:#fff;padding:16px 30px}
.wait h3{font-family:"Roboto Condensed",sans-serif;font-weight:400;font-size:28px;color:#666}
.wait-row{display:flex;align-items:center;gap:12px;margin-top:14px}
.wait-num{width:53px;height:50px;background:var(--teal);color:#fff;font-family:"Roboto Condensed",sans-serif;font-size:40px;display:flex;align-items:center;justify-content:center}
.wait-row span{font-family:"Roboto Condensed",sans-serif;font-weight:700;font-size:24px;color:var(--teal)}
.wait p{font-size:12px;line-height:18px;color:#777;margin-top:20px}
.bottombar{left:0;top:1451px;width:1050px;height:36px;background:var(--teal-dark);color:#fff;font-family:"Roboto Condensed",sans-serif;font-size:13px}
.foot-brand{left:99px;top:9px;display:flex;align-items:center;gap:7px;font-weight:700;font-size:13px;letter-spacing:.3px;white-space:nowrap}
.foot-brand i{width:14px;height:14px;background:#fff;display:block}
.copy{left:275px;top:11px;white-space:nowrap}
.legal{right:81px;top:11px}
</style>
</head>
<body>
<div class="page">
  <div class="abs topbar"></div>
  <div class="abs connect">Connect: <i class="social first"></i><i class="social"></i><i class="social"></i><i class="social"></i><i class="social"></i></div>
  <div class="abs utility">
    <svg width="14" height="14" viewBox="0 0 14 14"><circle cx="5" cy="5" r="3.5" fill="none" stroke="#f2652b" stroke-width="1.5"/><path d="M8 8l4 4" stroke="#f2652b" stroke-width="1.5"/></svg>
    <svg width="14" height="14" viewBox="0 0 14 14"><path d="M1 4h5l1 1h6v7H1z" fill="#bbb"/></svg>
    <svg width="14" height="14" viewBox="0 0 14 14"><text x="3" y="12" font-size="13" fill="#bbb" font-family="Roboto">?</text></svg>
  </div>

  <div class="abs brand"><span class="brand-mark"></span>NOVA MEDICAL CENTER</div>
  <nav class="abs nav"><a class="active" href="#">WHY NOVA</a><a href="#">PHYCISIANS</a><a href="#">SPECIALTIES</a><a href="#">INFO</a><a href="#">LOCATIONS</a><a href="#">CONTACT</a></nav>

  <div class="abs hero" role="img" aria-label="Photo of a smiling physician in a white coat with colleagues and a patient in a bright clinic"></div>
  <div class="abs hero-caption">Physician Owned. Patient-Focused</div>

  <div class="abs qc-head">
    <h2>QUICK CONTACT</h2>
    <div class="qc-phone"><span class="ic"><svg width="14" height="14" viewBox="0 0 14 14"><path d="M3 1l3 3-1.5 1.5c1 2 2 3 4 4L10 8l3 3-2 2C6 12 2 8 1 3z" fill="#fff"/></svg></span>(214) 555-0136</div>
  </div>
  <div class="abs qc-form"></div>
  <div class="abs or">OR</div>
  <div class="abs field" style="top:221px">Full Name:</div>
  <div class="abs field" style="top:260px">Phone Number:</div>
  <div class="abs field" style="top:300px">Email Address:</div>
  <div class="abs field msg" style="top:339px">Message:</div>
  <div class="abs btn submit">Submit Request</div>

  <div class="abs apart">What Sets Us Apart</div>
  <svg class="abs" style="left:195px;top:605px" width="68" height="48" viewBox="0 0 68 48"><path d="M3 6c10 18 32 22 58 20" fill="none" stroke="#777" stroke-width="1.5"/><path d="M46 14l16 12-22 18" fill="none" stroke="#777" stroke-width="1.5"/></svg>

  <div class="abs feature" style="left:275px">
    <div class="icon"><svg width="26" height="30" viewBox="0 0 26 30"><circle cx="13" cy="12" r="6" fill="none" stroke="#fff" stroke-width="2"/><path d="M10 19h6v5h-6z" fill="#fff"/><path d="M13 1v3M3 5l2 2M23 5l-2 2" stroke="#fff" stroke-width="2"/></svg></div>
    <h3>Technology</h3>
    <p>Ut enim ad minim veniam, quis nos ation ullamco laboris nisi ut aliq do consequat duis aute.</p>
  </div>
  <div class="abs feature" style="left:517px">
    <div class="icon"><svg width="28" height="24" viewBox="0 0 28 24"><rect x="2" y="6" width="24" height="17" rx="2" fill="#fff"/><rect x="9" y="2" width="10" height="5" fill="none" stroke="#fff" stroke-width="2"/><path d="M14 10v9M9.5 14.5h9" stroke="#49a7bc" stroke-width="3"/></svg></div>
    <h3>Quality of Care</h3>
    <p>Ut enim ad minim veniam, quis nos ation ullamco laboris nisi ut aliq do consequat duis aute.</p>
  </div>
  <div class="abs feature" style="left:758px">
    <div class="icon"><svg width="30" height="30" viewBox="0 0 30 30"><path d="M6 3v8c0 5 4 8 8 8M14 3v8" fill="none" stroke="#fff" stroke-width="2.5"/><path d="M12 19c2 6 8 7 11 2" fill="none" stroke="#fff" stroke-width="2.5"/><circle cx="23" cy="17" r="3.5" fill="none" stroke="#fff" stroke-width="2.5"/></svg></div>
    <h3>Patient Experience</h3>
    <p>Ut enim ad minim veniam, quis nos ation ullamco laboris nisi ut aliq do consequat duis aute.</p>
  </div>

  <div class="abs band"></div>
  <div class="abs team" role="img" aria-label="Photo of a team of three doctors and a nurse standing together"></div>
  <div class="abs about">
    <h2 class="sec">Heading Goes Here</h2>
    <p>Atiam porta sem malesuada magna mollis euismod.</p>
    <p>Nemo enim ipsam voluptatem, quia voluptas sit, aspernatur aut odit aut fugit, sed quia conse quuntur consequun. turmagni dolores eos.</p>
    <p>Fusce dapibus, tellus ac cursus commodo, tellus ac cursus commodo, tortor mauris condimentum nibh. Imt fermentum massa justo sit amet risus. Id elit non mi porta gravida at eget metus.</p>
  </div>
  <div class="abs testi">
    <h2 class="sec">Testimonials</h2>
    <p>Fusce dapibus, tellus ac cursus commodo, tellus ac cursus commodo, tortor mauris condimentum nibh. Imt fermentum massa justo sit amet risus. Id elit non mi porta gravida at eget metus.</p>
    <p>Atiam porta sem malesuada magna mollis euismod.</p>
  </div>
  <svg class="abs testi-tail" width="64" height="28" viewBox="0 0 64 28"><path d="M0 1h64M40 1L6 26z" fill="#fff" stroke="#ddd"/><path d="M40 0L6 26 14 0z" fill="#fff"/></svg>
  <div class="abs testi-author">Marcus – Finance Director</div>

  <div class="abs cta"></div>
  <div class="abs call"><svg width="20" height="22" viewBox="0 0 20 22"><path d="M4 1l5 5-2.5 2.5c1.5 3 3.5 5 6.5 6.5L15.5 12.5l4 4.5-3 3C8 18 3 12 1 4z" fill="#49a7bc"/></svg>Call Us: (214) 555-0136</div>
  <div class="abs divider"></div>
  <div class="abs nl-label">NEWSLETTER SIGN UP</div>
  <div class="abs nl-input">Enter your email</div>
  <div class="abs btn subscribe">SUBSCRIBE <svg width="18" height="13" viewBox="0 0 18 13"><rect x="1" y="1" width="16" height="11" fill="none" stroke="#fff" stroke-width="1.5"/><path d="M1 1l8 6 8-6" fill="none" stroke="#fff" stroke-width="1.5"/></svg></div>

  <div class="abs footer"></div>
  <div class="abs fcol" style="left:99px">
    <h3>News</h3>
    <div class="item"><div class="date"><b>25</b><small>Aug</small></div><div>Atiam porta sem malesuada magna mollis euismod.</div></div>
    <div class="item"><div class="date"><b>25</b><small>Aug</small></div><div>Atiam porta sem malesuada magna mollis euismod.</div></div>
    <div class="item"><div class="date"><b>25</b><small>Aug</small></div><div>Atiam porta sem malesuada magna mollis euismod.</div></div>
  </div>
  <div class="abs fcol" style="left:291px">
    <h3>Blog</h3>
    <div class="item"><div class="date plain"><b>25</b><small>Aug</small></div><div>Atiam porta sem malesuada magna mollis euismod.</div></div>
    <div class="item"><div class="date plain"><b>25</b><small>Aug</small></div><div>Atiam porta sem malesuada magna mollis euismod.</div></div>
    <div class="item"><div class="date plain"><b>25</b><small>Aug</small></div><div>Atiam porta sem malesuada magna mollis euismod.</div></div>
  </div>
  <div class="abs fcol" style="left:488px">
    <h3>Locations</h3>
    <div class="loc">Atiam porta sem malesuada magna mollis euismod.</div>
    <div class="loc">Atiam porta sem malesuada magna mollis euismod.</div>
    <div class="loc">Atiam porta sem malesuada magna mollis euismod.</div>
    <div class="loc">Atiam porta sem malesuada magna mollis euismod.</div>
  </div>
  <div class="abs wait">
    <h3>Average Wait Time</h3>
    <div class="wait-row"><div class="wait-num">9</div><span>Minutes</span></div>
    <p>Atiam porta sem malesuada magna mollis euismod. Nemo enim ipsam voluptatem, quia voluptas sit, asperna tur aut odit aut fugit, sed quia conse quuntur consequun.</p>
  </div>

  <div class="abs bottombar">
    <div class="abs foot-brand"><i></i>NOVA MEDICAL CENTER</div>
    <div class="abs copy">© 2013 &nbsp;All Rights Reserved</div>
    <div class="abs legal">Sitemap &nbsp;| &nbsp;Privacy</div>
  </div>
</div>
</body>
</html>
```